HR Outsourcing and Payroll Company needs a website re-design

The client is VireloStaffHR: www .virelostaff. example

They provide services to other businesses, specifically Human Resources (HR) Outsourcing and Payroll services. They are not happy with their current website and have retained our agency to provide a re-design.

You will design 4 pages for us to show the client. They will select a design they like. My agency will take the winning design and files and design the remaining pages of the site. But, we need you to help us establish a design for the basics so they can select a direction.

We need a Homepage design, a Service Page design, a Broker page design, and a Contact page design.

They really like these websites (in order from most preferred look and feel of imagery and design elements), so I think a mix between the two would be great:

https://www.brandleworks.example/
http://www.quopaly.example/

I have attached a project brief for this website. Please refer to it... It will help you be successful in what you deliver. The best designs will incorporate functionality and elements from the project brief.

Target Market(s)

Business owners. They will be thinking about thinks like employee reviews, payroll, time keeping, hiring, being compliant with state laws, and needing an expert to help them.

Industry/Entity Type

It Company

Number of Pages Required

4 page

Font styles to use
Sans Serif

Colors
f37122
0255a3
fbed22
9bcb3c
ec1f27

Requirements
Must have
• We need:
• -Homepage design (desktop and mobile)
• -Service Page design (desktop and mobile)
• -Broker page design (desktop and mobile)
• -Contact page design (desktop and mobile)
• Inspiration: a mix between the two would be great:
• https://www.brandleworks.example/
• http://www.quopaly.example/
• They like the long extended homepage look:
• http://www.quopaly.example/
• Photos that have focused people in the front and blurred backgrounds. Example: https://www.brandleworks.example/
• Graphic Icons for their services. Example:
• http://www.quopaly.example/
• I have attached a project brief for this website. Please refer to it... It will help you be successful in what you deliver. The best designs will incorporate functionality and elements from the project brief.
Should not have
• Crappy stock photos... you can use watermarked stock photos if you don't wish to purchase them for the sake of the contest.

```html
<!DOCTYPE html>
<html lang="en">
<head>
<meta charset="utf-8">
<title>VireloStaffHR – Human Resources</title>
<link rel="stylesheet" href="https://fonts.googleapis.com/css2?family=Raleway:wght@400;500;600;700;800&family=Open+Sans:wght@400;600;700&display=swap">
<style>
:root{
  --blue:#1c5aa6;
  --blue-line:#1f4f99;
  --gold:#c0873a;
  --gold-dark:#a9742f;
  --ink:#1d1d1d;
  --muted:#6b6b6b;
  --page:#f4f4f4;
  --white:#ffffff;
  --navy:#0f1d2e;
  --navy-deep:#0a1522;
  --slate:#2f3a48;
  --band:#55595e;
  --field:#121212;
}
*{box-sizing:border-box;margin:0;padding:0}
html,body{width:1200px;height:3291px;overflow:hidden}
body{position:relative;background:var(--page);font-family:"Open Sans",Arial,sans-serif;color:var(--ink)}
.abs{position:absolute}
a{color:inherit;text-decoration:none}

/* header */
.top-rule{left:0;top:0;width:1200px;height:7px;background:var(--blue)}
.site-header{left:0;top:7px;width:1200px;height:131px;background:var(--white)}
.brand{left:79px;top:36px;font-family:"Raleway",sans-serif;font-weight:700;font-size:40px;color:var(--blue);letter-spacing:.5px;display:flex;align-items:center;gap:12px}
.brand-dot{width:18px;height:18px;border-radius:50%;background:var(--gold)}
.util-nav{right:94px;top:28px;display:flex;gap:0;align-items:center;font-size:13px;letter-spacing:1px;color:#333}
.util-nav a{padding:0 14px;border-right:1px solid #bbb}
.util-nav a:last-of-type{border-right:1px solid #888}
.util-nav svg{margin-left:14px}
.main-nav{left:512px;top:86px;display:flex;gap:28px;font-family:"Raleway",sans-serif;font-weight:600;font-size:16px;letter-spacing:.5px;color:#111}
.btn{display:flex;align-items:center;justify-content:center;background:var(--gold);color:var(--white);font-family:"Raleway",sans-serif;font-weight:700;letter-spacing:1px;text-transform:uppercase}
.btn-start{left:961px;top:81px;width:158px;height:42px;font-size:15px;font-weight:600;box-shadow:0 2px 3px rgba(0,0,0,.25)}

/* hero */
.hero{left:0;top:138px;width:1200px;height:470px;background:linear-gradient(90deg,#d9dde4 0%,#c2c9d3 35%,#8f9aa8 60%,#b8c0cb 85%,#d6dbe2 100%)}
.hero-title{left:476px;top:376px;font-family:"Raleway",sans-serif;font-weight:400;font-size:60px;line-height:60px;color:var(--white);letter-spacing:2px}
.hero-sub{left:480px;top:440px;font-family:"Raleway",sans-serif;font-weight:400;font-size:38px;line-height:40px;color:var(--white);letter-spacing:1.5px}
.btn-assess{left:458px;top:509px;width:233px;height:51px;font-size:16px;font-weight:600}
.slider-arrow{top:292px;width:40px;height:110px;background:var(--white);display:flex;align-items:center;justify-content:center}
.arrow-prev{left:0}.arrow-next{right:0}

/* services */
.intro{left:0;top:648px;width:1200px;text-align:center;font-family:"Raleway",sans-serif;font-weight:600;font-size:25px;line-height:36px;color:var(--blue)}
.service-card{top:761px;width:194px;height:391px;background:var(--white);border-top:3px solid var(--blue-line);box-shadow:0 1px 3px rgba(0,0,0,.08)}
.service-icon{position:absolute;left:64px;top:22px}
.service-title{position:absolute;left:0;top:110px;width:100%;text-align:center;font-family:"Raleway",sans-serif;font-weight:600;font-size:15px;line-height:20px;color:#222}
.service-list{position:absolute;left:26px;top:146px;width:150px;list-style:none;font-size:11.5px;line-height:17px;color:var(--muted)}
.service-list li{position:relative;padding-left:14px;margin-bottom:9px}
.service-list li::before{content:"";position:absolute;left:0;top:7px;width:5px;height:5px;border-radius:50%;background:#9a9a9a}
.btn-card{position:absolute;left:32px;top:322px;width:140px;height:37px;font-size:13px}

/* stats */
.stats{left:0;top:1220px;width:1200px;height:360px;background:linear-gradient(180deg,#3a4350 0%,#2a323d 50%,#343c48 100%)}
.stats-heading{left:0;top:1263px;width:1200px;text-align:center;font-family:"Raleway",sans-serif;font-weight:600;font-size:25px;color:var(--white)}
.stat{top:1344px;width:160px;text-align:center;color:var(--white)}
.stat svg{display:block;margin:0 auto}
.stat-num{font-family:"Raleway",sans-serif;font-weight:700;font-size:22px;margin-top:18px;letter-spacing:1px}
.stat-label{font-size:11px;line-height:18px;margin-top:10px;font-weight:600;color:#e6e6e6}

/* blog */
.blog{left:0;top:1580px;width:1200px;height:592px;background:#f1f1f1}
.blog-heading{left:0;top:1614px;width:1200px;text-align:center;font-family:"Raleway",sans-serif;font-weight:600;font-size:31px;color:var(--blue)}
.post{top:1690px;width:318px}
.post-title{font-family:"Raleway",sans-serif;font-weight:800;font-size:18px;letter-spacing:1px;color:#111}
.post-excerpt{margin-top:10px;font-size:15px;line-height:22px;color:#555}
.post-photo{margin-top:20px;width:318px;height:210px}
.post-more{margin-top:22px;font-family:"Raleway",sans-serif;font-weight:700;font-size:17px;letter-spacing:1.5px;color:var(--gold)}
.btn-load{left:518px;top:2087px;width:160px;height:44px;font-size:17px}

/* testimonial */
.band{left:0;width:1200px;height:16px;background:var(--band)}
.testimonial{left:0;top:2194px;width:1200px;height:347px;background:linear-gradient(100deg,#3c4552 0%,#555e6a 55%,#6d7682 100%)}
.quote-mark{font-family:"Raleway",sans-serif;font-weight:800;font-size:110px;line-height:1;color:var(--white)}
.quote-text{left:140px;top:2290px;width:530px;font-family:"Raleway",sans-serif;font-weight:700;font-size:18.5px;line-height:29px;color:var(--white)}
.quote-author{left:140px;top:2420px;font-family:"Raleway",sans-serif;font-weight:700;font-size:21px;color:var(--gold)}
.partner-badge{left:838px;top:2236px;width:254px;height:254px;border-radius:50%;background:var(--white);border:6px solid var(--blue)}
.dots{left:535px;top:2510px;display:flex;gap:18px}
.dots span{width:17px;height:17px;border-radius:50%;background:var(--white)}
.dots span.active{background:var(--gold)}

/* contact */
.contact{left:0;top:2563px;width:1200px;height:370px;background:var(--white)}
.contact-heading{left:0;top:2583px;width:1200px;text-align:center;font-family:"Raleway",sans-serif;font-weight:600;font-size:32px;color:var(--blue)}
.field{height:46px;background:var(--field);color:#d8d8d8;font-family:"Raleway",sans-serif;font-weight:600;font-size:14px;display:flex;align-items:center;padding-left:12px}
.btn-send{left:496px;top:2857px;width:204px;height:46px;font-size:14px}

/* footer */
.footer-rule{left:0;top:2933px;width:1200px;height:11px;background:var(--gold)}
.site-footer{left:0;top:2944px;width:1200px;height:288px;background:var(--navy)}
.footer-brand{left:79px;top:3000px;font-family:"Raleway",sans-serif;font-weight:700;font-size:30px;color:var(--blue)}
.footer-h{font-family:"Raleway",sans-serif;font-weight:700;font-size:16px;letter-spacing:.5px;color:var(--white)}
.footer-links{list-style:none;font-family:"Raleway",sans-serif;font-weight:600;font-size:13.5px;letter-spacing:1.5px;color:#d0d4da}
.footer-links li{margin-top:21px}
.contact-line{font-size:14px;color:#d0d4da;margin-top:20px;letter-spacing:.3px}
.social{display:flex;gap:8px;margin-top:22px}
.social span{width:27px;height:27px;background:var(--gold)}
.about-text{margin-top:16px;width:220px;font-family:"Raleway",sans-serif;font-weight:600;font-size:14px;line-height:21px;color:#c8ccd2}
.signup-label{left:79px;top:3086px;font-family:"Raleway",sans-serif;font-weight:700;font-size:16px;color:var(--white)}
.signup-input{left:79px;top:3122px;width:217px;height:33px;background:var(--white);display:flex;align-items:center;gap:10px;padding-left:10px;font-size:13px;color:#999}
.btn-sub{left:79px;top:3166px;width:217px;height:37px;font-size:13px}
.legal{left:0;top:3232px;width:1200px;height:59px;background:var(--navy-deep);display:flex;align-items:center;justify-content:center;font-family:"Raleway",sans-serif;font-weight:700;font-size:15px;letter-spacing:1px;color:var(--white)}
.legal em{font-style:normal;color:var(--gold);margin-left:14px}
</style>
</head>
<body>

<div class="abs top-rule"></div>
<header class="abs site-header"></header>
<div class="abs brand"><span>VireloStaffHR</span><span class="brand-dot"></span></div>
<nav class="abs util-nav">
  <a href="#">LOGIN</a><a href="#">REGISTER</a>
  <svg width="22" height="22" viewBox="0 0 22 22"><circle cx="9" cy="9" r="6.5" fill="none" stroke="#555" stroke-width="2"/><line x1="14" y1="14" x2="20" y2="20" stroke="#555" stroke-width="2.4"/></svg>
</nav>
<nav class="abs main-nav"><a href="#">HOME</a><a href="#">SERVICES</a><a href="#">BROKERS</a><a href="#">CONTACT US</a></nav>
<a class="abs btn btn-start" href="#">Get Started</a>

<section class="abs hero" role="img" aria-label="Smiling businesswoman holding a red folder in front of a blurred group of colleagues"></section>
<div class="abs hero-title">GET YOUR FREE</div>
<div class="abs hero-sub">HR ASSESSMENT</div>
<a class="abs btn btn-assess" href="#">Take Assessment</a>
<div class="abs slider-arrow arrow-prev"><svg width="22" height="28" viewBox="0 0 22 28"><path d="M17 3 L5 14 L17 25" fill="none" stroke="#111" stroke-width="5"/></svg></div>
<div class="abs slider-arrow arrow-next"><svg width="22" height="28" viewBox="0 0 22 28"><path d="M5 3 L17 14 L5 25" fill="none" stroke="#111" stroke-width="5"/></svg></div>

<p class="abs intro">Gain a competitive advantage with the most trusted<br>and most used HR solutions and services.</p>

<article class="abs service-card" style="left:79px">
  <svg class="service-icon" width="66" height="66" viewBox="0 0 66 66" fill="none" stroke="#c0873a" stroke-width="3"><circle cx="33" cy="14" r="6"/><path d="M24 32c0-6 4-10 9-10s9 4 9 10"/><circle cx="12" cy="30" r="4"/><circle cx="54" cy="30" r="4"/><circle cx="20" cy="50" r="4"/><circle cx="46" cy="50" r="4"/><ellipse cx="33" cy="56" rx="22" ry="6"/></svg>
  <h3 class="service-title">HR Outsourcing</h3>
  <ul class="service-list"><li>Industry specialization</li><li>Decades of domain expertise</li><li>Employee onboarding</li><li>Benefits enrollment</li></ul>
  <a class="btn btn-card" href="#">Load More</a>
</article>
<article class="abs service-card" style="left:291px">
  <svg class="service-icon" width="66" height="66" viewBox="0 0 66 66"><path d="M33 6 L54 14 V32 C54 46 44 56 33 60 C22 56 12 46 12 32 V14 Z" fill="none" stroke="#c0873a" stroke-width="4"/><path d="M33 6 V60 C22 56 12 46 12 32 V14 Z" fill="#c0873a"/><circle cx="46" cy="48" r="10" fill="#c0873a"/><path d="M41 48 L45 52 L52 44" fill="none" stroke="#fff" stroke-width="3"/></svg>
  <h3 class="service-title">Safety</h3>
  <ul class="service-list"><li>Tax remitting and filing</li><li>Real-time entry</li><li>Payroll preview</li><li>Direct deposit</li></ul>
  <a class="btn btn-card" href="#">Load More</a>
</article>
<article class="abs service-card" style="left:503px">
  <svg class="service-icon" width="66" height="66" viewBox="0 0 66 66"><circle cx="33" cy="33" r="28" fill="#c0873a"/><circle cx="33" cy="33" r="21" fill="none" stroke="#fff" stroke-width="3"/><path d="M33 18 V34 H44" fill="none" stroke="#fff" stroke-width="4"/></svg>
  <h3 class="service-title">Payroll / Timekeeping</h3>
  <ul class="service-list"><li>Health care insurance</li><li>Retirement plans</li><li>Flexible spending accounts</li><li>COBRA</li></ul>
  <a class="btn btn-card" href="#">Load More</a>
</article>
<article class="abs service-card" style="left:715px">
  <svg class="service-icon" width="66" height="66" viewBox="0 0 66 66" fill="#c0873a"><rect x="20" y="8" width="26" height="20" rx="2"/><rect x="6" y="40" width="12" height="20"/><path d="M18 42 H36 C42 42 44 48 38 48 H30 L50 44 C58 42 60 48 54 50 L36 58 H18 Z"/></svg>
  <h3 class="service-title">Benefits<br>Administration</h3>
  <ul class="service-list"><li>Employment Practices Liability Insurance (EPLI)</li><li>Unemployment</li><li>Affordable Care Act (ACA) support</li></ul>
  <a class="btn btn-card" href="#">Load More</a>
</article>
<article class="abs service-card" style="left:927px">
  <svg class="service-icon" width="66" height="66" viewBox="0 0 66 66" fill="#c0873a"><path d="M22 16 C22 8 44 8 44 16 Z"/><rect x="20" y="16" width="26" height="3"/><circle cx="33" cy="26" r="8"/><path d="M14 60 C14 44 22 38 33 38 C44 38 52 44 52 60 Z"/><path d="M30 40 L42 52 L38 56 L26 44 Z" fill="#fff"/></svg>
  <h3 class="service-title">Workers'<br>Compensation</h3>
  <ul class="service-list"><li>Mobile app</li><li>Robust reporting</li><li>Time off tracking</li><li>Expense reimbursement</li></ul>
  <a class="btn btn-card" href="#">Load More</a>
</article>

<section class="abs stats" role="img" aria-label="Dim city skyline photograph behind the company statistics"></section>
<h2 class="abs stats-heading">We're passionate about our partners' success and empowering HR professionals.</h2>
<div class="abs stat" style="left:72px">
  <svg width="54" height="54" viewBox="0 0 54 54" fill="none" stroke="#c0873a" stroke-width="3"><path d="M16 6 H38 V20 C38 28 33 32 27 32 C21 32 16 28 16 20 Z"/><path d="M16 10 H8 C8 20 12 24 17 24 M38 10 H46 C46 20 42 24 37 24"/><path d="M27 32 V42 M18 48 H36 V42 H18 Z"/></svg>
  <div class="stat-num">7/10</div>
  <div class="stat-label">7 of the top 10 brokers on<br>the Broker Ledger 100<br>list partner with Brandleworks</div>
</div>
<div class="abs stat" style="left:257px">
  <svg width="54" height="54" viewBox="0 0 54 54" fill="#c0873a"><path d="M2 22 L14 12 L26 20 L20 26 L14 22 Z"/><path d="M52 22 L40 12 L26 20 L34 34 C36 36 40 34 38 32 L42 30 L52 24 Z"/><path d="M12 28 L26 42 L30 38 L16 26 Z"/></svg>
  <div class="stat-num">650</div>
  <div class="stat-label">Insurance brokers and<br>and payroll bureaus<br>partner with Brandleworks</div>
</div>
<div class="abs stat" style="left:446px">
  <svg width="66" height="54" viewBox="0 0 66 54" fill="#c0873a"><circle cx="33" cy="16" r="9"/><path d="M16 46 C16 32 24 28 33 28 C42 28 50 32 50 46 Z"/><circle cx="13" cy="20" r="7"/><path d="M0 44 C0 32 6 30 13 30 C17 30 20 31 22 33 C18 36 16 40 15 44 Z"/><circle cx="53" cy="20" r="7"/><path d="M66 44 C66 32 60 30 53 30 C49 30 46 31 44 33 C48 36 50 40 51 44 Z"/></svg>
  <div class="stat-num">94,000</div>
  <div class="stat-label">Employers nationwide</div>
</div>
<div class="abs stat" style="left:637px">
  <svg width="54" height="54" viewBox="0 0 54 54" fill="#c0873a"><circle cx="27" cy="14" r="10"/><path d="M6 52 C6 32 16 26 27 26 C38 26 48 32 48 52 Z"/><path d="M24 26 L27 44 L30 26 Z" fill="#2f3a48"/></svg>
  <div class="stat-num">13,000+</div>
  <div class="stat-label">SMB customers</div>
</div>
<div class="abs stat" style="left:805px">
  <svg width="54" height="54" viewBox="0 0 54 54" fill="none" stroke="#c0873a" stroke-width="4"><circle cx="27" cy="27" r="22"/><circle cx="27" cy="27" r="13"/><circle cx="27" cy="27" r="4" fill="#c0873a"/><path d="M27 27 L48 6" stroke-width="3"/></svg>
  <div class="stat-num">25</div>
  <div class="stat-label">Years in business</div>
</div>
<div class="abs stat" style="left:974px">
  <svg width="54" height="54" viewBox="0 0 54 54" fill="#c0873a"><rect x="8" y="36" width="8" height="14"/><rect x="20" y="28" width="8" height="22"/><rect x="32" y="20" width="8" height="30"/><path d="M6 28 L22 14 L30 20 L44 6" fill="none" stroke="#c0873a" stroke-width="3"/><path d="M38 4 H48 V14 Z"/></svg>
  <div class="stat-num">$31 Billion+</div>
  <div class="stat-label">Payroll managed annually</div>
</div>

<section class="abs blog"></section>
<h2 class="abs blog-heading">Recent Blog Posts</h2>
<article class="abs post" style="left:79px">
  <h3 class="post-title">PELLENTESQUE HABITANT</h3>
  <p class="post-excerpt">Your budget is configured for optimum learning outcomes.</p>
  <div class="post-photo" role="img" aria-label="Colleagues meeting around a bright office table" style="background:linear-gradient(135deg,#e8e2da,#b9a996 60%,#6d6a6a)"></div>
  <div class="post-more">READ MORE</div>
</article>
<article class="abs post" style="left:439px">
  <h3 class="post-title">PELLENTESQUE HABITANT</h3>
  <p class="post-excerpt">Your budget is configured for optimum learning outcomes.</p>
  <div class="post-photo" role="img" aria-label="Team discussing work at a laptop in a meeting room" style="background:linear-gradient(135deg,#f0f0f0,#9ea3a8 55%,#3c4450)"></div>
  <div class="post-more">READ MORE</div>
</article>
<article class="abs post" style="left:799px">
  <h3 class="post-title">PELLENTESQUE HABITANT</h3>
  <p class="post-excerpt">Your budget is configured for optimum learning outcomes.</p>
  <div class="post-photo" role="img" aria-label="Businessman in a suit reviewing papers" style="background:linear-gradient(135deg,#2c3a52,#5d6a80 55%,#c9ccd2)"></div>
  <div class="post-more">READ MORE</div>
</article>
<a class="abs btn btn-load" href="#">Load More</a>

<div class="abs band" style="top:2172px;height:22px"></div>
<section class="abs testimonial" role="img" aria-label="Faded photograph of financial charts and documents"></section>
<div class="abs quote-mark" style="left:82px;top:2220px">&ldquo;</div>
<blockquote class="abs quote-text">I love calling VIRELOSTAFFHR because I know I'm going to get a direct answer about HR issues and not a lot of legal garble. They just 'get to it'- so I can get back to business.</blockquote>
<div class="abs quote-author">Dana Whitfield, Director of HR</div>
<div class="abs quote-mark" style="left:636px;top:2400px">&rdquo;</div>
<div class="abs partner-badge"></div>
<div class="abs dots"><span class="active"></span><span></span><span></span><span></span></div>
<div class="abs band" style="top:2541px;height:22px;border-top:6px solid #fff"></div>

<section class="abs contact"></section>
<h2 class="abs contact-heading">Talk to a Team Member Today</h2>
<div class="abs field" style="left:263px;top:2666px;width:332px">First Name</div>
<div class="abs field" style="left:606px;top:2666px;width:322px">Last Name</div>
<div class="abs field" style="left:263px;top:2727px;width:332px">Company</div>
<div class="abs field" style="left:606px;top:2727px;width:322px">Phone</div>
<div class="abs field" style="left:263px;top:2789px;width:665px">Email</div>
<a class="abs btn btn-send" href="#">Send Your Message</a>

<div class="abs footer-rule"></div>
<footer class="abs site-footer"></footer>
<div class="abs footer-brand">VireloStaffHR</div>
<div class="abs signup-label">Sign up for fresh Insights:</div>
<div class="abs signup-input"><svg width="18" height="13" viewBox="0 0 18 13"><rect width="18" height="13" fill="#999"/><path d="M0 0 L9 7 L18 0" fill="none" stroke="#fff" stroke-width="1.5"/></svg>Email Adress</div>
<a class="abs btn btn-sub" href="#">Subscribe</a>

<div class="abs" style="left:408px;top:2984px">
  <div class="footer-h">NAVIGATION</div>
  <ul class="footer-links"><li>HOME</li><li>SERVICES</li><li>BROKERS</li><li>CONTACT US</li></ul>
</div>
<div class="abs" style="left:641px;top:2984px">
  <div class="footer-h">CONTACT US</div>
  <div class="contact-line">info@virelostaff.example</div>
  <div class="contact-line">(012) 555 0190</div>
  <div class="social"><span></span><span></span><span></span><span></span><span></span></div>
</div>
<div class="abs" style="left:902px;top:2984px">
  <div class="footer-h">ABOUT BUSINESS</div>
  <p class="about-text">Lorem ipsum dolor sit amet, consec-tetur adipisicing elit, sed do elusmod tempor et incididunt ut labore et dolore</p>
</div>

<div class="abs legal">2016 RK Halden, Inc. All rights reserved <em>PRIVACY POLICY &amp; TERMS OF USE</em></div>

</body>
</html>
```